ベースの色はグリーンですが、その系統の配色か、必要に応じては青をいれてもらってもかまいません。コーポレートサイトのデザインですが、色々な方のパターンを見てみたいです。
採用も目的としているため比較的爽やかなイメージが良いかもしれません。
仕様書【ミライワークス用】.pdfと添付画像をもとにデザイン作成お願いします。

当選前提となった方は正式な社名及び連絡先をお伝えしますので修正対応をお願いします。
また希望の際は、当選後、中ページの制作及びコーディングも別途ご依頼可能です。
ページ数
1ページ
希望イメージ
シンプル 複雑
単色 カラフル
暗い 明るい
日常 高級
遊び心 厳粛
未来的 伝統的
女性的 男性的
希望する色
緑系、青系
納品ファイル
• 高解像度JPG (.jpg)
• フォトショップ形式 (.psd)
弊社で納品している運送系サイトを参考までに記載します。

https://www.harunomiya.co.jp/
https://www.mido-hakobi.co.jp/
https://www.tachibe-web.co.jp/
https://www.renkaru.net/
■ 選んだ理由

採用を意識したイメージと、全体のメリハリ感が非常にマッチしておりました。
ありがとうございます。

■ 提案者全員のお礼・コメント

たくさんのご提案ありがとうございます。
どれも非常にレベルが高く弊社デザイナー感でも意見が割れて迷いました。
またの機会がありましたらよろしくお願いいたします。

```html
<!DOCTYPE html>
<html lang="ja">
<head>
<meta charset="UTF-8">
<title>株式会社〇〇運送</title>
<link rel="stylesheet" href="https://fonts.googleapis.com/css2?family=Noto+Sans+JP:wght@400;500;700&family=Oswald:wght@600;700&display=swap">
<style>
:root{
  --green:#0f6b3c;
  --green-dark:#0b5630;
  --green-light:#7cc242;
  --ink:#222;
  --gray:#f2f2f2;
  --footer:#2d2d2d;
  --white:#fff;
}
*{box-sizing:border-box;margin:0;padding:0}
html,body{width:1200px;height:3584px;overflow:hidden}
body{font-family:"Noto Sans JP",sans-serif;color:var(--ink);background:var(--white);position:relative}
.site-header{position:absolute;top:0;left:0;width:1200px;height:110px;background:var(--green);color:var(--white);display:flex;align-items:center;padding:0 40px}
.brand small{display:block;font-size:13px;letter-spacing:1px}
.brand strong{font-size:30px;font-weight:700;letter-spacing:2px}
.header-right{margin-left:auto;text-align:right}
.header-tel{font-size:22px;font-weight:700;display:flex;align-items:center;justify-content:flex-end;gap:8px}
.header-tel span{font-size:12px;font-weight:400;margin-left:10px}
.global-nav{display:flex;gap:30px;align-items:center;margin-top:10px;font-size:14px}
.nav-btn{background:var(--white);color:var(--green);padding:8px 22px;border-radius:3px;font-weight:700}
.hero{position:absolute;top:110px;left:0;width:1200px;height:650px;background:linear-gradient(90deg,#9cb5a0 0%,#c9d4d7 40%,#dfe5e8 70%,#b7c3cb 100%)}
.hero-text{position:absolute;left:130px;top:400px;color:var(--white)}
.hero-text .lead{font-size:24px;font-weight:500;letter-spacing:3px}
.hero-text h1{font-family:"Oswald",sans-serif;font-size:76px;line-height:1.1;letter-spacing:1px}
.hero-text p{font-size:14px;margin-top:6px}
.leaf-band{position:absolute;top:760px;left:0;width:1200px;height:220px;background:radial-gradient(circle at 30% 50%,#c8ec6a,#6fb531 55%,#3f8a22)}
.cert-box{position:absolute;left:300px;top:60px;width:600px;height:100px;background:var(--white);display:flex;align-items:center;padding:0 26px;gap:20px;font-size:13px;line-height:1.7}
.cert-mark{flex:none;width:64px;height:64px;border-radius:50%;background:#4db4d8}
.business{position:absolute;top:980px;left:0;width:1200px;height:520px;background:linear-gradient(160deg,var(--gray) 0 60%,var(--white) 60%)}
.section-title{font-size:32px;font-weight:700;letter-spacing:3px}
.section-sub{font-family:"Oswald",sans-serif;font-size:13px;letter-spacing:2px;color:#666;margin-top:4px}
.business-text{position:absolute;left:175px;top:110px;width:440px}
.business-text p{font-size:14px;line-height:2;margin-top:30px}
.btn{display:inline-block;background:var(--green);color:var(--white);font-size:14px;padding:10px 0;width:200px;text-align:center;border-radius:2px}
.business-text .btn{margin-top:40px}
.business-photo{position:absolute;left:640px;top:80px;width:560px;height:400px;background:linear-gradient(180deg,#cfe0ec,#8a9aa8 60%,#5c6570)}
.cards{position:absolute;top:1580px;left:120px;display:flex;gap:28px}
.card{width:300px}
.card-img{height:240px}
.card-label{display:flex;align-items:center;gap:6px;font-size:18px;font-weight:700;margin-top:14px}
.card-label::before{content:"";width:8px;height:8px;background:var(--green);border-radius:50%}
.card small{font-family:"Oswald",sans-serif;font-size:11px;color:#777;letter-spacing:1px;padding-left:14px}
.recruit{position:absolute;top:2020px;left:0;width:1200px;height:620px;background:linear-gradient(90deg,#2b5d4a,#4e7f6a 45%,#c8d2d6 60%,#9fb3c6)}
.recruit-panel{position:absolute;left:0;top:0;width:700px;height:620px;background:rgba(15,107,60,.82);clip-path:polygon(0 0,100% 0,72% 100%,0 100%)}
.recruit-text{position:absolute;left:120px;top:80px;color:var(--white)}
.recruit-text .section-sub{color:#d8eee0}
.recruit-text p{font-size:14px;line-height:2;margin-top:24px;width:440px}
.recruit-text .btn{background:var(--white);color:var(--green);margin-top:30px}
.recruit-people{position:absolute;left:640px;top:60px;width:480px;height:560px;background:linear-gradient(180deg,#6a9fd8,#2e66b8)}
.contact{position:absolute;top:2640px;left:0;width:1200px;height:520px;background:linear-gradient(180deg,#e8eef2,#c4ccd3)}
.contact-box{position:absolute;left:220px;top:100px;width:760px;height:320px;background:var(--white);text-align:center;padding-top:50px}
.contact-box p{font-size:13px;line-height:2;margin-top:24px}
.contact-box .btns{display:flex;gap:40px;justify-content:center;margin-top:30px}
.site-footer{position:absolute;top:3160px;left:0;width:1200px;height:424px;background:var(--footer);color:var(--white);text-align:center;padding-top:60px}
.site-footer .name{font-size:24px;font-weight:700;letter-spacing:2px}
.footer-nav{display:flex;gap:44px;justify-content:center;font-size:13px;margin-top:40px}
.footer-address{font-size:14px;line-height:1.8;margin-top:32px}
.footer-tel{display:inline-flex;align-items:center;gap:8px;background:var(--white);color:var(--ink);font-weight:700;font-size:18px;padding:8px 34px;border-radius:30px;margin-top:14px}
.copyright{font-size:11px;color:#aaa;margin-top:44px}
</style>
</head>
<body>
<header class="site-header">
  <div class="brand"><small>キャッチコピーテキスト</small><strong>株式会社〇〇運送</strong></div>
  <div class="header-right">
    <div class="header-tel">
      <svg width="20" height="20" viewBox="0 0 24 24"><path fill="#fff" d="M6.6 10.8a15 15 0 006.6 6.6l2.2-2.2c.3-.3.7-.4 1-.2 1.1.4 2.3.6 3.6.6.6 0 1 .4 1 1V20c0 .6-.4 1-1 1A17 17 0 013 4c0-.6.4-1 1-1h3.5c.6 0 1 .4 1 1 0 1.3.2 2.5.6 3.6.1.3 0 .7-.2 1z"/></svg>
      000-0000-0000<span>平日9:00〜17:00</span>
    </div>
    <nav class="global-nav"><span>ホーム</span><span>事業案内</span><span>環境品質方針</span><span>車両案内</span><span>採用情報</span><span>会社案内</span><span class="nav-btn">お問い合わせ</span></nav>
  </div>
</header>

<section class="hero" role="img" aria-label="駐車場に並ぶトラックの写真">
  <div class="hero-text">
    <div class="lead">安全・安心・信頼される企業として</div>
    <h1>RELIABILITY AND SAFETY</h1>
    <p>地域の物流を支える企業として、安全運行を第一に、確かな輸送サービスを提供し続けます。</p>
  </div>
</section>

<section class="leaf-band" role="img" aria-label="緑の葉の写真">
  <div class="cert-box">
    <p>弊社は、業界団体が定める安全評価制度において「安全運行認定事業所」の認定を受けております。安全性の高いサービスを提供するため、日々の運行管理を徹底しています。</p>
    <div class="cert-mark" aria-label="認定マーク"></div>
  </div>
</section>

<section class="business">
  <div class="business-text">
    <h2 class="section-title">事業内容</h2>
    <p>テキストテキストテキストテキストテキストテキストテキストテキストテキストテキストテキストテキストテキストテキストテキストテキストテキストテキストテキストテキストテキスト</p>
    <span class="btn">詳細はこちら</span>
  </div>
  <div class="business-photo" role="img" aria-label="整列したトラックの写真"></div>
</section>

<section class="cards">
  <div class="card"><div class="card-img" role="img" aria-label="双葉の新芽の写真" style="background:linear-gradient(180deg,#a6d84f,#3c8d2a)"></div><div class="card-label">環境・品質方針</div><small>POLICY</small></div>
  <div class="card"><div class="card-img" role="img" aria-label="赤いトラックの写真" style="background:linear-gradient(135deg,#b9d3ea,#c93a3a 55%,#7a2a2a)"></div><div class="card-label">車両案内</div><small>VEHICLES</small></div>
  <div class="card"><div class="card-img" role="img" aria-label="会社建物の写真" style="background:linear-gradient(180deg,#3f86cf,#d9e2ea 60%,#b7c2cc)"></div><div class="card-label">会社案内</div><small>ABOUT US</small></div>
</section>

<section class="recruit" role="img" aria-label="トラック前で作業着姿のスタッフの写真">
  <div class="recruit-panel"></div>
  <div class="recruit-people"></div>
  <div class="recruit-text">
    <h2 class="section-title">採用情報</h2>
    <div class="section-sub">RECRUIT</div>
    <p>私たちと一緒に働く仲間を募集しています。未経験の方も丁寧にサポートしますので、安心してご応募ください。</p>
    <span class="btn">詳細はこちら</span>
  </div>
</section>

<section class="contact" role="img" aria-label="白い会社建物の写真">
  <div class="contact-box">
    <h2 class="section-title">お問い合わせ</h2>
    <div class="section-sub">CONTACT</div>
    <p>弊社へのお問い合わせはお電話またはメールフォームよりお気軽にどうぞ。<br>担当者より折り返しご連絡いたします。</p>
    <div class="btns"><span class="btn">詳細はこちら</span><span class="btn">詳細はこちら</span></div>
  </div>
</section>

<footer class="site-footer">
  <div class="name">株式会社〇〇運送</div>
  <nav class="footer-nav"><span>ホーム</span><span>事業案内</span><span>環境品質方針</span><span>車両案内</span><span>採用情報</span><span>会社案内</span><span>お問い合わせ</span></nav>
  <div class="footer-address">〒000-0000<br>〇〇県〇〇市〇〇</div>
  <div class="footer-tel"><svg width="18" height="18" viewBox="0 0 24 24"><path fill="#222" d="M6.6 10.8a15 15 0 006.6 6.6l2.2-2.2c.3-.3.7-.4 1-.2 1.1.4 2.3.6 3.6.6.6 0 1 .4 1 1V20c0 .6-.4 1-1 1A17 17 0 013 4c0-.6.4-1 1-1h3.5c.6 0 1 .4 1 1 0 1.3.2 2.5.6 3.6.1.3 0 .7-.2 1z"/></svg>000-0000-0000</div>
  <div class="copyright">© 20XX 〇〇 All Rights Reserved.</div>
</footer>
</body>
</html>
```